Brennick Construction Core Values Wall Design

Core Values Wall Design for our Wall, I’m not exactly sure visually what we would want it to look like. Maybe some acrylic stand offs that could go on brick? If that’s a possibility. That’s where we have the most space in the office. But we could do other locations too.

These are our core values
• Safety
• Integrity
• Quality
• Client-Focused Solutions
• Continuous Improvement
• Positive Culture and Stewardship

Our vision/mission statement is Excellence Delivered.

```html
<!DOCTYPE html>
<html lang="en">
<head>
<meta charset="utf-8">
<title>Brennick Construction — Core Values</title>
<link href="https://fonts.googleapis.com/css2?family=Jost:wght@500;600;700&display=swap" rel="stylesheet">
<style>
  :root {
    --brand-blue: #1d5aa3;
    --brand-blue-deep: #17467f;
    --brand-red: #e3212d;
    --paper: #f4f3f6;
    --soft-blue: #b9cfe9;
    --soft-pink: #f1cdd6;
    --ink: #111111;
    --white: #ffffff;
  }
  html, body {
    margin: 0;
    padding: 0;
    overflow: hidden;
  }
  .canvas {
    position: relative;
    width: 1121px;
    height: 1200px;
    overflow: hidden;
    background: var(--paper);
    font-family: "Jost", "Futura", sans-serif;
  }
  .backdrop {
    position: absolute;
    inset: 0;
  }
  .company-name {
    position: absolute;
    top: 140px;
    left: 0;
    width: 100%;
    margin: 0;
    text-align: center;
    line-height: 1;
    font-weight: 600;
    color: var(--brand-blue);
  }
  .company-name-main {
    display: block;
    font-size: 84px;
    letter-spacing: 4px;
  }
  .company-name-sub {
    display: block;
    margin-top: 14px;
    font-size: 36px;
    letter-spacing: 20px;
    padding-left: 20px;
  }
  .values-wheel {
    position: absolute;
    inset: 0;
  }
  .mission-text {
    font-weight: 600;
    font-size: 31px;
    fill: var(--brand-blue);
  }
  .value-label {
    font-weight: 600;
    font-size: 25px;
    fill: var(--white);
    text-anchor: middle;
    letter-spacing: -0.5px;
  }
  .hub-label {
    font-weight: 600;
    font-size: 36px;
    fill: var(--ink);
    text-anchor: middle;
  }
  .seg-blue { fill: var(--brand-blue); }
  .seg-red { fill: var(--brand-red); }
  .icon { fill: var(--white); }
</style>
</head>
<body>
<div class="canvas">
  <svg class="backdrop" width="1121" height="1200" viewBox="0 0 1121 1200">
    <defs>
      <filter id="soften" x="-20%" y="-20%" width="140%" height="140%">
        <feGaussianBlur stdDeviation="6"/>
      </filter>
    </defs>
    <circle cx="150" cy="180" r="300" fill="var(--soft-blue)" opacity="0.8" filter="url(#soften)"/>
    <circle cx="440" cy="70" r="260" fill="var(--soft-blue)" opacity="0.45" filter="url(#soften)"/>
    <circle cx="980" cy="780" r="340" fill="var(--soft-pink)" opacity="0.75" filter="url(#soften)"/>
    <circle cx="760" cy="1180" r="260" fill="var(--soft-pink)" opacity="0.45" filter="url(#soften)"/>
  </svg>

  <h1 class="company-name">
    <span class="company-name-main">BRENNICK</span>
    <span class="company-name-sub">CONSTRUCTION</span>
  </h1>

  <svg class="values-wheel" width="1121" height="1200" viewBox="0 0 1121 1200">
    <defs>
      <path id="mission-arc" d="M262 590 A340 340 0 0 1 858 590"/>
    </defs>

    <circle cx="560" cy="745" r="372" fill="var(--white)" opacity="0.92"/>

    <text class="mission-text">
      <textPath href="#mission-arc" startOffset="50%" text-anchor="middle">Our Mission : Excellence Delivered</textPath>
    </text>

    <circle cx="560" cy="745" r="318" fill="var(--brand-blue-deep)"/>

    <g class="wheel-segments" stroke="var(--white)" stroke-width="3">
      <path class="seg-red"  d="M560 745 L560 432 A313 313 0 0 1 831 588.5 Z"/>
      <path class="seg-blue" d="M560 745 L831 588.5 A313 313 0 0 1 831 901.5 Z"/>
      <path class="seg-red"  d="M560 745 L831 901.5 A313 313 0 0 1 560 1058 Z"/>
      <path class="seg-blue" d="M560 745 L560 1058 A313 313 0 0 1 289 901.5 Z"/>
      <path class="seg-red"  d="M560 745 L289 901.5 A313 313 0 0 1 289 588.5 Z"/>
      <path class="seg-blue" d="M560 745 L289 588.5 A313 313 0 0 1 560 432 Z"/>
    </g>

    <circle cx="560" cy="745" r="112" fill="#000" opacity="0.1"/>
    <circle cx="560" cy="745" r="88" fill="var(--white)"/>
    <text class="hub-label" x="560" y="735">Core</text>
    <text class="hub-label" x="560" y="775">Values</text>

    <!-- Integrity -->
    <g class="icon">
      <path d="M438 518 h44 v32 l-22 12 l-22 -12 Z"/>
      <rect x="450" y="530" width="20" height="4" fill="var(--brand-blue)"/>
      <rect x="450" y="538" width="20" height="4" fill="var(--brand-blue)"/>
    </g>
    <text class="value-label" x="460" y="600">Integrity</text>

    <!-- Quality -->
    <g class="icon">
      <path d="M647 548 l-6 20 l8 -4 l5 6 l6 -18 Z"/>
      <path d="M673 548 l6 20 l-8 -4 l-5 6 l-6 -18 Z"/>
      <circle cx="660" cy="532" r="22"/>
      <circle cx="660" cy="532" r="15" fill="var(--brand-red)"/>
      <path d="M660 522 l3 7 l7 1 l-5 5 l1.5 7 l-6.5 -3.5 l-6.5 3.5 l1.5 -7 l-5 -5 l7 -1 Z"/>
    </g>
    <text class="value-label" x="660" y="608">Quality</text>

    <!-- Client Focused Solutions: handshake -->
    <g class="icon">
      <rect x="720" y="672" width="12" height="28" rx="2" transform="rotate(-35 726 686)"/>
      <rect x="788" y="672" width="12" height="28" rx="2" transform="rotate(35 794 686)"/>
      <path d="M732 684 c8 -8 16 -10 26 -6 c8 -4 16 -2 28 6 l-4 12 c-6 8 -14 14 -24 16 c-4 0 -8 -2 -12 -6 c-6 -4 -10 -10 -14 -14 Z"/>
      <path d="M748 690 l18 14 M754 686 l18 14 M742 696 l14 12" fill="none" stroke="var(--brand-blue)" stroke-width="2.5" stroke-linecap="round"/>
    </g>
    <text class="value-label" x="760" y="745">Client</text>
    <text class="value-label" x="760" y="775">Focused</text>
    <text class="value-label" x="760" y="805">Solutions</text>

    <!-- Safety -->
    <g class="icon">
      <path d="M645 868 l17 -6 l17 6 v14 c0 14 -8 22 -17 28 c-9 -6 -17 -14 -17 -28 Z"/>
      <path d="M653 884 l6 6 l12 -12" fill="none" stroke="var(--brand-red)" stroke-width="5" stroke-linecap="round" stroke-linejoin="round"/>
    </g>
    <text class="value-label" x="660" y="945">Safety</text>

    <!-- Continuous Improvement -->
    <g class="icon">
      <rect x="440" y="892" width="9" height="16"/>
      <rect x="453" y="884" width="9" height="24"/>
      <rect x="466" y="876" width="9" height="32"/>
      <rect x="436" y="909" width="44" height="4"/>
      <path d="M436 880 l18 -10 l10 6 l16 -12" fill="none" stroke="var(--white)" stroke-width="4"/>
      <path d="M476 858 l10 -2 l-2 10 Z"/>
    </g>
    <text class="value-label" x="460" y="948">Continuous</text>
    <text class="value-label" x="460" y="978">Improvement</text>

    <!-- Positive Culture and Stewardship -->
    <g class="icon">
      <rect x="343" y="678" width="8" height="22" rx="1"/>
      <path d="M354 700 v-22 l10 -10 l3 -10 c5 0 7 4 6 9 l-2 7 h12 c4 0 6 4 5 7 l-4 14 c-1 3 -3 5 -6 5 Z"/>
    </g>
    <text class="value-label" x="360" y="735">Positive</text>
    <text class="value-label" x="360" y="765">Culture and</text>
    <text class="value-label" x="360" y="795">Stewardship</text>
  </svg>
</div>
</body>
</html>
```